Folder and Swag Design for Law Firm

We are a personal injury law firm designing new client materials for folders and other swag that will go to clients once they retain us. Rather than just being white on green, or green on white, we'd like a design to put on the items. One idea that we had was a wave that included our slogan of "Our family protecting yours" that can wrap around a folder, or a tumbler but we are open to other ideas. I've attached a sketch of the wave design and our logo.
The final design should communicate a family protective feel.
Branding colors: #FFFFFF, #0FA57B, #00CA88
Victims of personal injury (car accidents, slip and falls, defective products).
Legal Services

```html
<!DOCTYPE html>
<html lang="en">
<head>
<meta charset="utf-8">
<title>Harlow &amp; Pierce, LLC — Client Folder</title>
<link rel="stylesheet" href="https://fonts.googleapis.com/css2?family=Marcellus&family=Kaushan+Script&display=swap">
<style>
  :root {
    --green: #3aa57b;
    --deep: #1b363c;
    --white: #ffffff;
    --page: #ffffff;
    --ghost: rgba(255, 255, 255, 0.04);
  }
  html, body {
    margin: 0;
    padding: 0;
    width: 882px;
    height: 1200px;
    overflow: hidden;
    background: var(--page);
  }
  .canvas {
    position: relative;
    width: 882px;
    height: 1200px;
  }
  .folder-dieline {
    position: absolute;
    left: 20px;
    top: 224px;
    width: 842px;
    height: 751px;
  }
  .panel-outside { fill: var(--green); }
  .panel-cover { fill: var(--deep); }
  .wave-deep, .pocket { fill: var(--deep); }
  .wave-band { fill: var(--white); }
  .wave-green { fill: var(--green); }
  .brand-square { fill: var(--green); }
  .ghost-square { fill: var(--ghost); }
  .firm-name {
    font-family: "Marcellus", serif;
    font-size: 25px;
    letter-spacing: 1px;
    fill: var(--green);
  }
  .firm-tagline {
    font-family: "Marcellus", serif;
    font-size: 10px;
    letter-spacing: 2.5px;
    fill: var(--white);
  }
  .slogan {
    font-family: "Kaushan Script", cursive;
    font-size: 38px;
    fill: var(--green);
  }
</style>
</head>
<body>
<main class="canvas">
  <svg class="folder-dieline" viewBox="272 1200 1110 990" xmlns="http://www.w3.org/2000/svg" aria-label="Flat folder layout with pocket">
    <!-- back (outside) panel -->
    <rect class="panel-outside" x="320" y="1205" width="530" height="710"/>
    <path class="wave-deep" d="M320,1833 C400,1810 480,1805 560,1830 C650,1860 760,1860 850,1835 L850,1915 L320,1915 Z"/>

    <!-- front cover panel -->
    <rect class="panel-cover" x="850" y="1205" width="530" height="710"/>
    <rect class="ghost-square" x="1012" y="1436" width="200" height="165"/>

    <g class="brand-lockup">
      <rect class="brand-square" x="920" y="1272" width="95" height="78"/>
      <text class="firm-name" x="1028" y="1319">HARLOW &amp; PIERCE, LLC</text>
      <text class="firm-tagline" x="1098" y="1341">ATTORNEYS AT LAW</text>
    </g>

    <path class="wave-band" d="M850,1725 C930,1695 1010,1700 1090,1720 C1180,1740 1280,1740 1380,1735 L1380,1850 C1300,1875 1220,1870 1150,1855 C1050,1825 950,1820 850,1835 Z"/>
    <path class="wave-green" d="M850,1835 C950,1820 1050,1825 1150,1855 C1220,1870 1300,1875 1380,1850 L1380,1915 L850,1915 Z"/>

    <path id="slogan-line" fill="none" d="M905,1782 C1000,1762 1080,1768 1150,1798 C1220,1825 1280,1822 1340,1808"/>
    <text class="slogan"><textPath href="#slogan-line">Our family protecting yours</textPath></text>

    <!-- pocket flap -->
    <path class="pocket" d="M320,1925 L292,1925 L275,1940 L275,2165 L295,2185 L530,2185 C700,2180 796,2075 798,1915 L320,1915 Z"/>
  </svg>
</main>
</body>
</html>
```